Need a new updated business logo and business cards and possible car signs. Logo should be modern with bold elements. Possible use in some way of former logo may be considered. Looking for use of bold colors to grab attention with car signage/wrap in mind. Phone number should be easy to read- customers should understand what business is about- home painting, repair, renovation, 're-imagine your space' etc.

Target Market(s)

Homeowners, construction, businesses

Industry/Entity Type

Contractor

Contact Information for Business Card

Brennick Painting & Renovation, Inc.
Owner : Marcus D. Brennick
919-555-0173
marcusdbrennickmb@larkpost.com
All work is guaranteed and insured! More than 30 years of experience:
residential & commercial, Interior & Exterior, Renovation/Restoration

Logo Text

Brennick Painting & Renovation, Inc. 'Hard Working & Trustworthy'

Other font styles liked:
• Designer suggestions for industry

Colors

Designer to choose colors to be used in the design.

Requirements
Must have
• New design logo-possibly incorporating old elements- new logo ok without old though as well. Cell Phone number has to be on there- Color preferable
Nice to have
• Nice to have a logo that pops and that may be used in conjunction with his parent company Brennick HOLM Estates, LLC.
• Business card layout of information that is clear & easy to read
Should not have
• Bulky old fonts

```html
<!DOCTYPE html>
<html lang="en">
<head>
<meta charset="utf-8">
<title>Brennick Painting &amp; Renovation – Business Cards</title>
<link href="https://fonts.googleapis.com/css2?family=Lato:wght@400;700;900&display=swap" rel="stylesheet">
<style>
  :root {
    --brand-red: #a50f12;
    --band-red: #a8161a;
    --paper: #ffffff;
    --ink: #2d2d2d;
    --stage: #e4e4e6;
    --soft-white: rgba(255,255,255,0.9);
    --rule: rgba(255,255,255,0.35);
  }
  * { box-sizing: border-box; margin: 0; padding: 0; }
  html, body { width: 1200px; height: 900px; overflow: hidden; }
  body {
    background: var(--stage);
    font-family: 'Lato', sans-serif;
    position: relative;
  }
  .card {
    position: absolute;
    left: 250px;
    width: 700px;
    height: 400px;
    border-radius: 34px;
    overflow: hidden;
    box-shadow: 0 10px 24px rgba(0,0,0,0.18);
  }
  .card--back { top: 30px; background: var(--brand-red); color: var(--paper); text-align: center; }
  .card--front { top: 470px; background: var(--paper); color: var(--ink); }

  .wordmark { font-family: 'Lato', sans-serif; font-weight: 900; letter-spacing: 2px; line-height: 1; }
  .wordmark__name { font-size: 62px; }
  .wordmark__sub { font-size: 17px; font-weight: 400; letter-spacing: 1px; margin-top: 6px; }

  .card--back .wordmark { margin-top: 92px; }
  .back__rule { width: 400px; height: 1px; background: var(--rule); margin: 20px auto 18px; }
  .back__tagline { font-size: 20px; line-height: 1.55; color: var(--soft-white); }

  .front__brand { position: absolute; left: 48px; top: 44px; color: var(--brand-red); }
  .front__brand .wordmark__sub { color: var(--ink); }
  .front__address { position: absolute; right: 48px; top: 48px; text-align: right; font-size: 22px; line-height: 1.3; }
  .front__person { position: absolute; left: 48px; top: 168px; }
  .person__name { color: var(--brand-red); font-size: 30px; font-weight: 400; letter-spacing: 2px; }
  .person__role { font-size: 17px; margin-top: 2px; }
  .contact { list-style: none; margin-top: 16px; font-size: 21px; }
  .contact li { display: flex; align-items: center; gap: 10px; line-height: 1.4; }
  .contact svg { width: 18px; height: 18px; flex: none; }
  .front__band {
    position: absolute; left: 0; right: 0; bottom: 0; height: 62px;
    background: var(--band-red); color: var(--paper);
    display: flex; align-items: center; justify-content: center;
    font-weight: 700; font-size: 19px; letter-spacing: 1px;
  }
</style>
</head>
<body>
  <section class="card card--back">
    <div class="wordmark">
      <div class="wordmark__name">BRENNICK'S</div>
      <div class="wordmark__sub">PAINTING &amp; RENOVATION, INC</div>
    </div>
    <div class="back__rule"></div>
    <p class="back__tagline">More than 30 years of experience.<br>Residential &amp; commercial | Interior &amp; Exterior<br>Renovation/Restoration</p>
  </section>

  <section class="card card--front">
    <div class="wordmark front__brand">
      <div class="wordmark__name">BRENNICK'S</div>
      <div class="wordmark__sub">PAINTING &amp; RENOVATION, INC</div>
    </div>
    <address class="front__address" style="font-style:normal">48 Harlow Court<br>Fairmont, NC 27099</address>
    <div class="front__person">
      <div class="person__name">MARCUS D. BRENNICK</div>
      <div class="person__role">Owner</div>
      <ul class="contact">
        <li>
          <svg viewBox="0 0 18 18" aria-hidden="true"><rect x="4" y="1" width="10" height="16" rx="2" fill="none" stroke="#a50f12" stroke-width="2"/><circle cx="9" cy="14" r="1.2" fill="#a50f12"/></svg>
          919-555-0173
        </li>
        <li>
          <svg viewBox="0 0 18 18" aria-hidden="true"><rect x="1" y="3" width="16" height="12" fill="#a50f12"/><path d="M1 3 L9 10 L17 3" fill="none" stroke="#fff" stroke-width="1.5"/></svg>
          marcusdbrennickmb@larkpost.com
        </li>
      </ul>
    </div>
    <div class="front__band">ALL WORK IS GUARANTEED AND INSURED!</div>
  </section>
</body>
</html>
```